electrical contractor business card for professional modern company

I need a business card design for an electrical contractors business. I do all kinds of electricical work from new homes, air conditioning, data and communications. I have a logo design i want on it and have a good idea in my head of what i want it to look like. I like simple yet bold and professional looking. All black background is a must

Target Market(s)

Anyone needing electrical work done

Industry/Entity Type

Electrical

Contact Information for Business Card

company name- KMP Electrical and Data
person name-lewis pembury
phone number- 0468 239 517
website-kmpwire-sample.com.au

Font styles to use
Sans Serif

Requirements
Must have
• email
• website
• logo
• name
• phone number
• list of work i do:
• -electrical
• -air-conditioning
• -data/communications
• -cctv/security
• -domestic/commercial/industrial
• -24hr emergency breakdown repair
Nice to have
• i would like the logo on the front side in the centre taking up most of the card with black background.
• on the rear i want the list of work i do with company info i.e. email, website, my name, phone number. rear of card also black background with orange writing to match the orange in the logo

```html
<!DOCTYPE html>
<html lang="en">
<head>
<meta charset="utf-8">
<title>KMP Electrical and Data – Business Card</title>
<link rel="stylesheet" href="https://fonts.googleapis.com/css2?family=Saira:wght@500;600&display=swap">
<style>
  :root {
    --page-bg: #d9d9d9;
    --card-black: #0b0b0b;
    --card-back: #1c1c1c;
    --brand-orange: #e2661d;
    --text-white: #f2f2f2;
    --card-shadow: rgba(0, 0, 0, 0.28);
  }
  * { box-sizing: border-box; margin: 0; padding: 0; }
  html, body {
    width: 1200px;
    height: 900px;
    overflow: hidden;
  }
  body {
    background: radial-gradient(ellipse at center, #e6e6e6 0%, var(--page-bg) 70%, #c9c9c9 100%);
    font-family: "Saira", "Arial", sans-serif;
    position: relative;
  }
  .card {
    position: absolute;
    left: 310px;
    width: 580px;
    height: 354px;
    border-radius: 3px;
    box-shadow: 0 10px 26px var(--card-shadow);
    overflow: hidden;
  }

  /* Front */
  .card-front {
    top: 70px;
    background: var(--card-black);
    display: flex;
    align-items: center;
    justify-content: center;
  }
  .brand-name {
    color: var(--brand-orange);
    font-weight: 600;
    text-transform: uppercase;
    text-align: center;
    line-height: 1;
  }
  .brand-name .brand-initials {
    display: block;
    font-size: 96px;
    letter-spacing: 6px;
  }
  .brand-name .brand-descriptor {
    display: block;
    font-size: 22px;
    letter-spacing: 3px;
    margin-top: 6px;
  }

  /* Back */
  .card-back {
    top: 476px;
    background: var(--card-back);
    color: var(--text-white);
  }
  .contact-block {
    position: absolute;
    left: 32px;
    top: 116px;
    width: 250px;
  }
  .contact-name {
    font-size: 20px;
    font-weight: 600;
    text-transform: uppercase;
    letter-spacing: 0.5px;
    line-height: 1.3;
    margin-bottom: 2px;
  }
  .contact-line {
    display: flex;
    align-items: center;
    gap: 7px;
    color: var(--brand-orange);
    font-size: 19px;
    font-weight: 600;
    line-height: 1.4;
    white-space: nowrap;
  }
  .contact-line svg {
    width: 12px;
    height: 12px;
    flex: none;
  }
  .divider {
    position: absolute;
    top: 42px;
    height: 200px;
    width: 4px;
  }
  .divider-white { left: 296px; background: var(--text-white); }
  .divider-orange { left: 305px; background: var(--brand-orange); }
  .services {
    position: absolute;
    left: 324px;
    top: 34px;
    width: 236px;
  }
  .services-title {
    font-size: 20px;
    font-weight: 600;
    text-transform: uppercase;
    letter-spacing: 0.5px;
    line-height: 1.2;
  }
  .services-list {
    list-style: none;
    color: var(--brand-orange);
    font-size: 16px;
    font-weight: 500;
    line-height: 1.12;
    white-space: nowrap;
  }
  .tagline {
    position: absolute;
    left: 0;
    right: 0;
    bottom: 30px;
    text-align: center;
    font-weight: 500;
  }
  .tagline-call {
    font-size: 15px;
    color: var(--text-white);
  }
  .tagline-values {
    font-size: 18px;
    color: var(--brand-orange);
    letter-spacing: 0.3px;
  }
</style>
</head>
<body>

  <section class="card card-front" aria-label="Business card front">
    <h1 class="brand-name">
      <span class="brand-initials">KMP</span>
      <span class="brand-descriptor">Electrical and Data</span>
    </h1>
  </section>

  <section class="card card-back" aria-label="Business card back">
    <div class="contact-block">
      <p class="contact-name">Lewis Pembury</p>
      <p class="contact-line">
        <svg viewBox="0 0 12 12" aria-hidden="true">
          <circle cx="6" cy="6" r="5.3" fill="none" stroke="#f2f2f2" stroke-width="1"/>
          <path d="M4 3.2 L5 3 L5.6 4.6 L5 5.1 C5.4 6 6 6.6 6.9 7 L7.4 6.4 L9 7 L8.8 8 C6.5 8.4 3.6 5.5 4 3.2 Z" fill="#f2f2f2"/>
        </svg>
        0468 239 517
      </p>
      <p class="contact-line">
        <svg viewBox="0 0 12 12" aria-hidden="true">
          <circle cx="6" cy="6" r="5.3" fill="none" stroke="#f2f2f2" stroke-width="1"/>
          <ellipse cx="6" cy="6" rx="2.3" ry="5.3" fill="none" stroke="#f2f2f2" stroke-width="0.8"/>
          <line x1="0.7" y1="6" x2="11.3" y2="6" stroke="#f2f2f2" stroke-width="0.8"/>
        </svg>
        kmpwire-sample.com.au
      </p>
    </div>

    <span class="divider divider-white" aria-hidden="true"></span>
    <span class="divider divider-orange" aria-hidden="true"></span>

    <div class="services">
      <h2 class="services-title">My Services:</h2>
      <ul class="services-list">
        <li>-electrical</li>
        <li>-air-conditioning</li>
        <li>-data/communications</li>
        <li>-cctv/security</li>
        <li>-domestic/commercial</li>
        <li>/industrial</li>
        <li>-24hr emergency</li>
        <li>breakdown repair</li>
      </ul>
    </div>

    <div class="tagline">
      <p class="tagline-call">Forget all you worries and call me!</p>
      <p class="tagline-values">Reliable. Experienced. Hard working.</p>
    </div>
  </section>

</body>
</html>
```